Kelmora Legal Business Card

I require a corporate business card for a new legal services business.

I do not have a logo, nor do I want one.

I require a clean, neat a professional card for a law firm.

Details:

Business Name: Kelmora Legal
Name: Debra Lindqvist
Title: Corporate Services Manager
Location: Office 14 (Top Floor), Toravel Business Centre, Quinlan Grove Street, Alotau CBD, Milne Bay Province.
Postal Address: PO Box 593, Alotau, 211, Milne Bay Province, Papua New Guinea.
Contact: T: +675 6418250, F: +675 6413362, M: +675 72915867, E: dlindqvist@kelmoraexample.com.pg.

I look forward to your design submissions.

Industry/Entity Type

Legal

```html
<!DOCTYPE html>
<html lang="en">
<head>
<meta charset="utf-8">
<title>Kelmora Legal Business Card</title>
<link href="https://fonts.googleapis.com/css2?family=Roboto+Condensed:wght@400;700&display=swap" rel="stylesheet">
<style>
  :root {
    --page-bg: #dcdcdc;
    --card-white: #ffffff;
    --brand-blue: #1f5ea8;
    --brand-blue-text: #1c4f93;
    --address-grey: #6b6b6b;
    --divider-grey: #7a7a7a;
    --on-blue: #ffffff;
  }
  html, body {
    margin: 0;
    padding: 0;
    width: 1200px;
    height: 1011px;
    overflow: hidden;
    background: var(--page-bg);
    font-family: "Roboto Condensed", "Arial Narrow", sans-serif;
  }
  .business-card {
    position: absolute;
    left: 350px;
    top: 95px;
    width: 500px;
    height: 820px;
    background: var(--brand-blue);
    overflow: hidden;
    box-shadow: 0 6px 18px rgba(0,0,0,0.18);
  }
  .card-cap {
    position: absolute;
    left: 0;
    top: 0;
    width: 500px;
    height: 330px;
  }
  .cap-header {
    position: absolute;
    top: 52px;
    right: 50px;
    text-align: right;
  }
  .firm-name {
    margin: 0 0 10px;
    color: var(--brand-blue-text);
    font-weight: 400;
    font-size: 38px;
    letter-spacing: 5px;
    text-transform: uppercase;
    line-height: 1;
  }
  .office-address {
    margin: 0;
    font-style: normal;
    color: var(--address-grey);
    font-size: 21px;
    line-height: 1.22;
  }
  .card-body {
    position: absolute;
    left: 95px;
    top: 372px;
    color: var(--on-blue);
  }
  .person-name {
    margin: 0;
    font-weight: 700;
    font-size: 27px;
    line-height: 1.1;
  }
  .person-title {
    margin: 2px 0 40px;
    font-size: 23px;
  }
  .contact-list {
    list-style: none;
    margin: 0;
    padding: 0;
    font-size: 23px;
    line-height: 1.2;
  }
  .contact-item {
    display: flex;
    align-items: flex-start;
    margin-bottom: 14px;
  }
  .contact-item.postal { margin-bottom: 24px; }
  .contact-icon {
    flex: 0 0 22px;
    width: 22px;
    height: 22px;
    margin: 2px 16px 0 0;
  }
</style>
</head>
<body>
  <div class="business-card">
    <svg class="card-cap" viewBox="0 0 500 330" aria-hidden="true">
      <path d="M0 0 H500 V210 Q250 360 0 210 Z" fill="#7a7a7a" transform="translate(0,6)"/>
      <path d="M0 0 H500 V210 Q250 360 0 210 Z" fill="#ffffff"/>
    </svg>

    <header class="cap-header">
      <h1 class="firm-name">Kelmora Legal</h1>
      <address class="office-address">
        Office 14 (Top Floor),<br>
        Toravel Business Centre,<br>
        Quinlan Grove Street,<br>
        Alotau CBD, Milne Bay Province
      </address>
    </header>

    <section class="card-body">
      <h2 class="person-name">Debra Lindqvist</h2>
      <p class="person-title">Corporate Services Manager</p>
      <ul class="contact-list">
        <li class="contact-item postal">
          <svg class="contact-icon" viewBox="0 0 24 24"><path d="M12 2a7 7 0 0 0-7 7c0 5 7 13 7 13s7-8 7-13a7 7 0 0 0-7-7zm0 9.5a2.5 2.5 0 1 1 0-5 2.5 2.5 0 0 1 0 5z" fill="#fff"/></svg>
          <span>PO Box 593, Alotau<br>211, Milne Bay Province<br>Papua New Guinea</span>
        </li>
        <li class="contact-item">
          <svg class="contact-icon" viewBox="0 0 24 24"><circle cx="12" cy="12" r="11" fill="#fff"/><path d="M8 6.5l2 2-1 1.5c.8 1.7 2 2.9 3.7 3.7l1.5-1 2 2-1.3 1.8c-3.6-.5-6.9-3.8-7.4-7.4z" fill="#1f5ea8"/></svg>
          <span>+675 6418250</span>
        </li>
        <li class="contact-item">
          <svg class="contact-icon" viewBox="0 0 24 24"><circle cx="12" cy="12" r="11" fill="#fff"/><rect x="7" y="10" width="10" height="7" fill="#1f5ea8"/><rect x="9" y="6" width="6" height="4" fill="none" stroke="#1f5ea8" stroke-width="1.3"/></svg>
          <span>+675 6413362</span>
        </li>
        <li class="contact-item">
          <svg class="contact-icon" viewBox="0 0 24 24"><circle cx="12" cy="12" r="11" fill="#fff"/><rect x="8.5" y="5.5" width="7" height="13" rx="1.3" fill="#1f5ea8"/><rect x="9.8" y="7.2" width="4.4" height="8" fill="#fff"/></svg>
          <span>+675 72915867</span>
        </li>
        <li class="contact-item">
          <svg class="contact-icon" viewBox="0 0 24 24"><circle cx="12" cy="12" r="11" fill="#fff"/><rect x="6.5" y="8" width="11" height="8" fill="#1f5ea8"/><path d="M6.5 8l5.5 4.5L17.5 8" fill="none" stroke="#fff" stroke-width="1.2"/></svg>
          <span>dlindqvist@kelmoraexample.com.pg</span>
        </li>
      </ul>
    </section>
  </div>
</body>
</html>
```